Ceramic worktop for laboratory furniture

We want a simple product catalog, maybe 4-8 pages, our ceramic worktop was chemical resistant, is a good worktop material for high chemicals corrosion environment like laboratory furniture, fumecupboard.

You can visit http://www.glazebenchsurface.com/products/PELM%20BENCH%20SURFACE%20PAIRED%20ITEMS.html
https://www.clipmesh.example/731902846551207/videos/6048215379012764/?__so__=channel_tab&__rv__=all_videos_card

http://www.benchora-gulf.example/products/lab-furniture-series/worktops#verticalTab3

https://www.quillbrookfitouts.example/blog/laboratory-countertop-material/

https://resources.tarnvalefabrication.example/blog/top-5-materials-to-consider-for-your-lab-countertops

https://www.morvik.example/blog/type-of-laboratory-worktops-their-selection-criteria/

https://www.brenholt.example/Brenholt/Literature/Blog/The-Different-Laboratory-Worksurfaces.htm

as reference

Target Market(s)

Asia, UAE and India

Industry/Entity Type

Laboratory fumecupboard and laboratory furniture manufacturer

Font styles to use
Sans Serif

Colors
00AB8E
00BBA5
67D7C9
C6EFE9
E9F9F6

Requirements
Must have
• This catalog mainly will sent to my customer handphone

```html
<!DOCTYPE html>
<html lang="en">
<head>
<meta charset="utf-8">
<title>Kestrel Lab Supplies – Laboratory Ceramic Worktop Catalogue</title>
<link href="https://fonts.googleapis.com/css2?family=Oswald:wght@300;400&family=Poppins:wght@400;500;600;700&display=swap" rel="stylesheet">
<style>
  :root {
    --green: #22a63a;
    --ink: #1d1d1d;
    --text: #333;
    --canvas: #dfe1df;
    --paper: #f1f2f1;
    --paper-light: #fbfbfb;
    --frame: #bfc2bf;
  }
  * { box-sizing: border-box; margin: 0; padding: 0; }
  html, body { width: 1109px; height: 1200px; overflow: hidden; background: var(--canvas); }
  body { position: relative; font-family: "Poppins", sans-serif; color: var(--text); }

  .page {
    position: absolute; width: 287px; height: 510px; overflow: hidden;
    background: linear-gradient(160deg, var(--paper-light), var(--paper) 55%, #e9eae9);
    box-shadow: 0 0 0 0.6px var(--frame);
  }
  .page > svg { position: absolute; left: 0; top: 0; width: 287px; height: 510px; }

  .p1 { left: 82px;  top: 82px; }
  .p2 { left: 407px; top: 82px; }
  .p3 { left: 727px; top: 82px; }
  .p4 { left: 82px;  top: 620px; }
  .p5 { left: 407px; top: 620px; }
  .p6 { left: 727px; top: 620px; }

  /* brand name */
  .brand {
    position: absolute; display: flex; align-items: center; gap: 4px;
    font-weight: 700; color: var(--ink); text-transform: uppercase; line-height: 1.05;
  }
  .brand .mark { background: var(--green); flex: none; }
  .brand-small { right: 14px; top: 26px; width: 70px; font-size: 8px; }
  .brand-small .mark { width: 8px; height: 8px; }
  .brand-cover { left: 86px; top: 40px; width: 112px; font-size: 14px; }
  .brand-cover .mark { width: 12px; height: 12px; }
  .brand-large { left: 62px; top: 66px; width: 170px; font-size: 20px; }
  .brand-large .mark { width: 16px; height: 16px; }

  /* section heading with bars */
  .section-title {
    position: absolute; left: 0; display: flex; align-items: center; gap: 4px;
    font-family: "Oswald", sans-serif; font-weight: 300; font-size: 17px; color: #222; line-height: 1;
  }
  .section-title .bar { height: 10px; background: var(--green); }
  .section-title .bar-end { height: 10px; background: var(--green); clip-path: polygon(0 0, 100% 0, 82% 100%, 0 100%); }

  /* cover */
  .cover-title {
    position: absolute; left: 82px; top: 386px;
    font-family: "Oswald", sans-serif; font-weight: 300; font-size: 37px; line-height: 36px; color: #fff;
  }

  /* thumbnails */
  .thumb { display: block; border: 0.8px solid var(--green); }

  /* furniture */
  .furniture-card { position: absolute; width: 112px; }
  .furniture-card .thumb { width: 103px; height: 77px; }
  .furniture-card h3 { font-size: 7.6px; font-weight: 600; color: var(--ink); margin: 10px 0 4px; line-height: 10px; }
  .furniture-card ul { list-style: none; }
  .furniture-card li { font-size: 6.4px; line-height: 8.8px; padding-left: 8px; position: relative; white-space: nowrap; }
  .furniture-card li::before {
    content: ""; position: absolute; left: 0; top: 2.7px; width: 3.4px; height: 3.4px;
    border: 1px solid var(--green); border-radius: 50%;
  }

  /* advantages */
  .advantage { position: absolute; font-size: 9px; line-height: 11px; color: #333; white-space: nowrap; }
  .advantage svg { display: block; width: 28px; height: 28px; margin-bottom: 6px; }

  /* product */
  .lead { position: absolute; left: 20px; top: 110px; width: 247px; text-align: center; font-size: 9px; line-height: 12px; color: #333; }
  .product-grid { position: absolute; left: 34px; top: 148px; display: grid; grid-template-columns: 105px 105px; gap: 11px 9px; }
  .product-grid .thumb { width: 105px; height: 79px; }

  /* colours */
  .size-note { position: absolute; left: 0; top: 101px; width: 287px; text-align: center; font-size: 9px; color: #333; }
  .swatch-row { position: absolute; left: 37px; font-size: 9px; line-height: 11px; color: #333; }
  .swatch { width: 71px; height: 18px; border: 0.8px solid var(--green); box-shadow: 1px 2px 3px rgba(0,0,0,.25); margin-bottom: 3px; }
  .swatch.white { background: #fff; }
  .swatch.grey { background: #c8c9c8; }
  .swatch.black { background: #1e1e1e; }
  .description { position: absolute; left: 145px; top: 136px; width: 124px; font-size: 7.4px; line-height: 10px; color: #333; }
  .description p + p { margin-top: 10px; }

  /* contact */
  .company { position: absolute; left: 66px; top: 204px; font-size: 9px; font-weight: 700; color: var(--ink); white-space: nowrap; }
  .company small { font-size: 5.2px; font-weight: 500; }
  .contact-list { position: absolute; left: 66px; top: 222px; font-size: 6.4px; line-height: 9px; color: #333; border-collapse: collapse; }
  .contact-list th { text-align: left; font-weight: 700; vertical-align: top; width: 27px; padding-bottom: 3.8px; }
  .contact-list td { vertical-align: top; padding-bottom: 3.8px; }
  .contact-list td.sep { width: 6px; font-weight: 700; }
  .contact-list td.value { width: 160px; }
</style>
</head>
<body>

<!-- Cover -->
<section class="page p1">
  <svg viewBox="0 0 287 510">
    <defs>
      <linearGradient id="coverPhoto" x1="0" y1="0" x2="0" y2="1">
        <stop offset="0" stop-color="#8f918d"/>
        <stop offset="0.35" stop-color="#c8c4bb"/>
        <stop offset="0.55" stop-color="#5c5c5a"/>
        <stop offset="1" stop-color="#3a3a39"/>
      </linearGradient>
    </defs>
    <polygon points="0,212 287,72 287,510 0,510" fill="url(#coverPhoto)" role="img" aria-label="Photo of a laboratory under fit-out with white cabinets and black ceramic worktops"/>
    <polygon points="65,0 287,0 287,68 65,166" fill="#fff" stroke="#22a63a" stroke-width="2.4"/>
    <line x1="0" y1="212" x2="287" y2="72" stroke="#22a63a" stroke-width="2.6"/>
    <polyline points="84,383 74,383 74,403" fill="none" stroke="#22a63a" stroke-width="1"/>
    <polyline points="207,496 217,496 217,476" fill="none" stroke="#22a63a" stroke-width="1"/>
  </svg>
  <div class="brand brand-cover"><span class="mark"></span><span>Kestrel Lab Supplies</span></div>
  <h1 class="cover-title">LABORATORY<br>CERAMIC<br>WORKTOP</h1>
</section>

<!-- Lab furniture -->
<section class="page p2">
  <svg viewBox="0 0 287 510" aria-hidden="true">
    <polygon points="0,0 76,0 287,94 287,0" fill="#fff" opacity="0.6"/>
    <line x1="76" y1="0" x2="287" y2="94" stroke="#22a63a" stroke-width="2.6"/>
  </svg>
  <div class="brand brand-small"><span class="mark"></span><span>Kestrel Lab Supplies</span></div>
  <h2 class="section-title" style="top:75px"><span class="bar" style="width:103px"></span>LAB FURNITURE<span class="bar-end" style="width:48px"></span></h2>

  <div class="furniture-card" style="left:27px;top:128px">
    <div class="thumb" style="background:linear-gradient(#dcdedd,#6d6f6e 60%,#bfc1c0)" role="img" aria-label="Photo of stainless steel lab tables with black tops"></div>
    <h3>Lab Tables</h3>
    <ul><li>Modular Systems</li><li>Lab Islands</li><li>Stainless Steel Tables</li><li>Mass Spec Benches</li><li>Microscope Tables</li><li>ESD Lab Tables</li><li>Balance &amp; Anti-Vibration Tables</li><li>Science Classroom Workstations</li></ul>
  </div>
  <div class="furniture-card" style="left:172px;top:128px">
    <div class="thumb" style="background:linear-gradient(#e6e7ea,#2c48a8 55%,#1d2f70)" role="img" aria-label="Photo of blue metal lab casework with instruments"></div>
    <h3>Lab Casework</h3>
    <ul><li>Metal Casework</li><li>Plastic Laminate Casework</li><li>Stainless Steel Casework</li><li>Cleanroom Casework</li><li>Phenolic Resin Casework</li><li>Anti-Microbial Casework</li><li>Veterianry Casework</li><li>Medical Casework</li><li>Classroom Casework</li></ul>
  </div>
  <div class="furniture-card" style="left:27px;top:316px">
    <div class="thumb" style="background:linear-gradient(#e4e5e4,#9a9c9a 55%,#cfd0cf)" role="img" aria-label="Photo of stainless steel countertops and wall cabinets"></div>
    <h3>Laboratory Countertops</h3>
    <ul><li>Epoxy Resin</li><li>Phenolic resin</li><li>Corvane Lab Grade Phenolic</li><li>High Density Polyethylene</li><li>Maple Black</li><li>Stainless Steel</li><li>Veltrex - CR</li><li>Halvern Solid Surface</li></ul>
  </div>
  <div class="furniture-card" style="left:172px;top:316px">
    <div class="thumb" style="background:linear-gradient(#f2f3f3,#d9dcdc 60%,#c4c7c7)" role="img" aria-label="Photo of an empty cleanroom with fume hoods"></div>
    <h3>Other Lab Furniture</h3>
    <ul><li>Fume Hoods</li><li>Biosafety Cabinets</li><li>Laboratory Chairs</li><li>Partitions and Dividers</li><li>Accessories</li></ul>
  </div>
</section>

<!-- Advantages -->
<section class="page p3">
  <svg viewBox="0 0 287 510">
    <polygon points="0,0 76,0 287,94 287,0" fill="#fff" opacity="0.6" aria-hidden="true"/>
    <line x1="76" y1="0" x2="287" y2="94" stroke="#22a63a" stroke-width="2.6"/>
    <polygon points="0,322 287,420 287,510 0,510" fill="#7a6a4f" role="img" aria-label="Photo of a long lab corridor with wooden cabinets and black ceramic worktops"/>
    <polygon points="0,390 287,470 287,510 0,510" fill="#c9a56e" opacity="0.7" aria-hidden="true"/>
    <line x1="0" y1="322" x2="287" y2="420" stroke="#22a63a" stroke-width="2"/>
  </svg>
  <div class="brand brand-small"><span class="mark"></span><span>Kestrel Lab Supplies</span></div>
  <h2 class="section-title" style="top:75px"><span class="bar" style="width:103px"></span>ADVANTAGES<span class="bar-end" style="width:48px"></span></h2>

  <div class="advantage" style="left:50px;top:100px">
    <svg viewBox="0 0 28 28" fill="none" stroke="#333" stroke-width="1.2"><rect x="3" y="16" width="20" height="4" rx="2"/><path d="M8 14 L20 6 L23 9 L11 16" stroke="#22a63a"/><circle cx="22" cy="20" r="1" fill="#333"/><circle cx="22" cy="24" r="1" fill="#333"/></svg>
    Corrosion Resistant
  </div>
  <div class="advantage" style="left:179px;top:100px">
    <svg viewBox="0 0 28 28" fill="none" stroke="#333" stroke-width="1.2"><path d="M6 2 V18 L10 26 H20 L22 16 L16 12 V8"/><path d="M4 2 H8" stroke="#22a63a"/></svg>
    Scratch Resistant
  </div>
  <div class="advantage" style="left:50px;top:160px">
    <svg viewBox="0 0 28 28" fill="none" stroke="#333" stroke-width="1.2"><path d="M14 4 C18 10 20 13 17 18 C15 20 11 19 11 16 C11 12 14 10 14 4Z"/><path d="M3 24 L8 19 H25 L20 24Z" stroke="#22a63a"/></svg>
    Fireproof upto 1200'c
  </div>
  <div class="advantage" style="left:179px;top:160px">
    <svg viewBox="0 0 28 28" fill="none" stroke="#333" stroke-width="1.2"><circle cx="14" cy="14" r="11" stroke="#22a63a"/><path d="M6 22 L22 6" stroke="#22a63a"/><circle cx="11" cy="12" r="2"/><circle cx="17" cy="16" r="2"/></svg>
    Antibacterial
  </div>
  <div class="advantage" style="left:50px;top:220px">
    <svg viewBox="0 0 28 28" fill="none" stroke="#333" stroke-width="1.2"><rect x="4" y="4" width="20" height="20" stroke="#22a63a" stroke-dasharray="2 2"/><rect x="8" y="8" width="12" height="12"/></svg>
    Non-deformation
  </div>
  <div class="advantage" style="left:179px;top:220px">
    <svg viewBox="0 0 28 28" fill="none" stroke="#333" stroke-width="1.2"><rect x="3" y="8" width="16" height="16" rx="3"/><path d="M22 2 V8 M19 5 H25 M24 11 V15 M22 13 H26" stroke="#22a63a"/></svg>
    Easy to clean
  </div>
  <div class="advantage" style="left:50px;top:280px">
    <svg viewBox="0 0 28 28" fill="none" stroke="#333" stroke-width="1.2"><circle cx="14" cy="14" r="12"/><path d="M14 6 C18 12 19 15 16 19 C13 21 10 18 12 14 C13 12 14 10 14 6Z" fill="#333"/></svg>
    Non-inflamable Class 1A
  </div>
  <div class="advantage" style="left:179px;top:280px">
    <svg viewBox="0 0 28 28" fill="none" stroke="#22a63a" stroke-width="1.2"><circle cx="8" cy="8" r="1.5"/><circle cx="14" cy="5" r="1.5"/><circle cx="20" cy="8" r="1.5"/><circle cx="11" cy="14" r="1.5"/><circle cx="17" cy="14" r="1.5"/><path d="M3 22 H25 M3 25 H25" stroke="#333"/></svg>
    Waterproof
  </div>
</section>

<!-- Product -->
<section class="page p4">
  <svg viewBox="0 0 287 510">
    <polygon points="0,0 76,0 287,94 287,0" fill="#fff" opacity="0.6" aria-hidden="true"/>
    <line x1="76" y1="0" x2="287" y2="94" stroke="#22a63a" stroke-width="2.6"/>
    <polygon points="0,320 287,421 287,510 0,510" fill="#e8e6e1" role="img" aria-label="Photo of a white worktop with sink over wood-finish cabinets"/>
    <polygon points="28,390 238,390 238,500 28,500" fill="#9b8a72" opacity="0.7" aria-hidden="true"/>
    <line x1="0" y1="320" x2="287" y2="421" stroke="#22a63a" stroke-width="2"/>
  </svg>
  <div class="brand brand-small"><span class="mark"></span><span>Kestrel Lab Supplies</span></div>
  <h2 class="section-title" style="top:75px"><span class="bar" style="width:112px"></span>PRODUCT<span class="bar-end" style="width:56px"></span></h2>
  <p class="lead">Laboratory work bench with Black and Grey colour ceramic worktop</p>
  <div class="product-grid">
    <div class="thumb" style="background:linear-gradient(#eceeee,#c7cacb)" role="img" aria-label="Photo of white lab benches with reagent shelves"></div>
    <div class="thumb" style="background:linear-gradient(#e9ebeb,#a9a49b)" role="img" aria-label="Photo of lab island with grey worktop"></div>
    <div class="thumb" style="background:linear-gradient(#e7eaea,#c9cdcd 60%,#3b9a9a)" role="img" aria-label="Photo of white bench with black worktop on teal floor"></div>
    <div class="thumb" style="background:linear-gradient(#dfe1e1,#2a2a2a 45%,#d8d9d9)" role="img" aria-label="Photo of white bench with black ceramic worktop"></div>
  </div>
</section>

<!-- Colours -->
<section class="page p5">
  <svg viewBox="0 0 287 510">
    <polygon points="0,0 76,0 287,94 287,0" fill="#fff" opacity="0.6" aria-hidden="true"/>
    <line x1="76" y1="0" x2="287" y2="94" stroke="#22a63a" stroke-width="2.6"/>
    <polygon points="0,320 287,421 287,510 0,510" fill="#6b6d6c" role="img" aria-label="Photo of a teaching lab with grey ceramic worktops and wooden cabinets"/>
    <polygon points="0,450 140,420 200,510 0,510" fill="#c9a56e" opacity="0.7" aria-hidden="true"/>
    <line x1="0" y1="320" x2="287" y2="421" stroke="#22a63a" stroke-width="2"/>
  </svg>
  <div class="brand brand-small"><span class="mark"></span><span>Kestrel Lab Supplies</span></div>
  <h2 class="section-title" style="top:75px"><span class="bar" style="width:115px"></span>COLORS<span class="bar-end" style="width:58px"></span></h2>
  <p class="size-note">Available in 2600 x 800 x 15 mm</p>
  <div class="swatch-row" style="top:136px"><div class="swatch white"></div>White</div>
  <div class="swatch-row" style="top:203px"><div class="swatch grey"></div>Grey</div>
  <div class="swatch-row" style="top:263px"><div class="swatch black"></div>Black</div>
  <div class="description">
    <p>Kestrel laboratory 15mm ceramic worktop are sintered at a high temperature of 1200 'c can truly achieve the same color of the body and glaze and avoid problems such as delamination and shedding. Ceramic worktop is corrosion- resistant, fireproff, waterproof, scratch-resistant, abrasion-resistant, non-deformation.</p>
    <p>Ceramic worktops can resist strong acid, alkaline and organic solvent corrosion (except of hydrofluoric acid equvilent chemical reagents).</p>
  </div>
</section>

<!-- Contact -->
<section class="page p6">
  <svg viewBox="0 0 287 510">
    <polygon points="0,319 287,400 287,510 0,510" fill="#d9c8a6" role="img" aria-label="Photo of a bright lab with black worktops beside a large window"/>
    <polygon points="60,360 150,380 150,440 60,430" fill="#9fb7c4" opacity="0.8" aria-hidden="true"/>
    <polygon points="130,460 287,430 287,470 130,500" fill="#222" opacity="0.85" aria-hidden="true"/>
  </svg>
  <div class="brand brand-large"><span class="mark"></span><span>Kestrel Lab Supplies</span></div>
  <h2 class="section-title" style="top:171px"><span class="bar" style="width:62px"></span>CONTACT US<span class="bar-end" style="width:74px"></span></h2>
  <p class="company">KESTREL LAB SUPPLIES SDN. BHD. <small>(902417-K)</small></p>
  <table class="contact-list">
    <tr><th>Add.</th><td class="sep">:</td><td class="value">No 12, Jalan Meranti 7/3, Off Jalan Sentosa, Batu 6, Seksyen 21, 40300 Taman Cendana, Selangor, Malaysia</td></tr>
    <tr><th>Tel</th><td class="sep">:</td><td class="value">+603 5210 4418, 6011-2974 5530/1/2</td></tr>
    <tr><th>Fax</th><td class="sep">:</td><td class="value">+603-5210 4419</td></tr>
    <tr><th>H/P</th><td class="sep">:</td><td class="value">+6012-3864102</td></tr>
    <tr><th>Web</th><td class="sep">:</td><td class="value">www.kestrellab.example</td></tr>
    <tr><th>Email</th><td class="sep">:</td><td class="value">hello@kestrellab.example</td></tr>
  </table>
</section>

</body>
</html>
```